Biker App Design
Zielgruppe
VeloMarn erstellt eine App für Biker mit der:
- Motorradfahrer andere Biker finden können um gemeinsam zu fahren
- Motorradfahrer ihre Strecke tracken können um Punkte zu sammeln
- Biker können mit diesen Punkten Ränge aufsteigen 'Masterbiker, Anfänger, GuruFahrer, etc.', es soll eine Art 'Erfahrungsleiste' angezeigt werden
- Diese Punkte können gegen Gutscheine/Wertsachen eingelöst werden
- Es gibt Nachrichten (Art Blogeinträge) genau zu diesen Themen
Aufgabenstellung
Modernes Design
Reduziert
Es werden folgende Screens benötigt:
Startbild
Start - Dateneintragen:
Um den Fahrer besser mit anderen Fahren zu verknüpfen muss er folgende informationen angeben:
- Welche Art Motorrad fährt er? Sport, Vintage, Cross
- Männlich/Weiblich/Divers
- Geburtsjahr
- PLZ des Heimatorts
- Nickname
Startscreen um andere Biker zu suchen und damit eine Tour zu starten
- Hier sollte ein 'Map' Bild mit einem Kreis für den Umkreis dargestellt werden + Pins mit Personenbilder , welche
Personen in der Nähe sind und auch fahren möchten
- Hier sollte stehen, wieviel Punkte er noch benötigt um den nächsten Gutschein freizuschalten
Screen zum Start des Trackens
Screen während dem Tracken mit Pause/Stop-Option
Screen mit einem Überblick der neuen Blogeinträge
Screen beim beenden des Trackens (Strecke speichern, Bild hinzufügen, Freunde informieren ich bin angekommen)
Screen Profilseite, Bild des Bikers + Bike + Erfahrungspunkte + gesammelte Errungenschaften z.B. 'Mit 3 Freunden mehr als 1000km gefahren'
Screen Bestenliste, anhand der Punkte
Es sollen Dateiformate verwendet werden, die gut wiederverwendet werden können. Es sollen sich Bausteine aus diesen Design wiederverwenden lassen können.
Wir benötigen eine APP mit einem User-Dashboards (Life-Account) in dem Finanz, Karriere und Gesundheitsthemen erkennbar sein sollen. Look and Feel soll seriös, schnörkelos und modern sein.
Das Design soll simpel sein. Also Verwendung von wenigen, dezenten Farben (Schattierungen / Blendeffekte erlaubt) und san-serife / simple schrift. Ich würde es mit progressiv, technisch, eher jugendlich, eher offen/frisch, modern, eher prägnant, clean, urban, eher freundschaftlich, schlicht, ehe..
hallo, wir brauchen das design für eine startseite. thema taxi app alle weiteren infos siehe anhang pdf eilauftrag - sofort kauf möglich danke
Unter Flickhafen.de kann das aktuelle Design angeschaut werden. Die Farbe sollten übernommen werden. Über die Startseite kann der Kunde sein Gerät, Service sowie seine Adresse eingeben. Auf der Vergleichsseite bekommt der Kunde die Übersicht welche Reparaturwerkstätten es gibt, zu welch..
Vorweg: Dem Auftrag folgen weitere Teilaufträge an den Gewinner, natürlich gegen Bezahlung. Für die bereits programmierte Webapplikation "tocks" wird ein Design benötigt. Tocks ähnelt den bereits bestehenden Zeiterfassungssystemen, soll sich aber anhand von Einfachheit, Speditivität und..

```html
<!DOCTYPE html>
<html lang="en">
<head>
<meta charset="utf-8">
<title>VeloMarn – Sign up</title>
<link rel="stylesheet" href="https://fonts.googleapis.com/css2?family=Roboto:wght@300;400;500&display=swap">
<style>
  :root{
    --stage:#1b1c1f;
    --status:#141517;
    --appbar:#1e1f22;
    --surface:#2c2e33;
    --text:#f2f2f2;
    --muted:#b9bbc0;
    --rule:rgba(255,255,255,.28);
    --brand:#e0262c;
    --button:#e8585f;
    --photo-light:#9a9c9f;
    --photo-dark:#3a3c40;
  }
  *{box-sizing:border-box;margin:0;padding:0}
  html,body{width:1200px;height:801px;overflow:hidden}
  body{background:var(--stage);font-family:"Roboto",sans-serif;color:var(--text);position:relative}
  .screen{position:absolute;left:397px;top:40px;width:405px;height:720px;background:var(--surface);overflow:hidden;border-radius:4px}
  .status-bar{position:absolute;left:0;top:0;width:100%;height:24px;background:var(--status);display:flex;justify-content:flex-end;align-items:center;gap:6px;padding-right:12px;font-size:13px;font-weight:500}
  .app-bar{position:absolute;left:0;top:24px;width:100%;height:54px;background:var(--appbar);display:flex;align-items:center;justify-content:center}
  .back{position:absolute;left:16px;top:17px}
  .brand-name{color:var(--brand);font-size:17px;font-weight:500;letter-spacing:.5px}
  .title{position:absolute;top:100px;width:100%;text-align:center;font-size:23px;font-weight:300}
  .hero-photo{position:absolute;left:0;top:268px;width:100%;height:452px;
    background:linear-gradient(160deg,var(--photo-dark) 0%,var(--photo-light) 45%,#6d6f73 70%,var(--photo-dark) 100%);opacity:.75}
  .field{position:absolute;left:32px;width:341px;border-bottom:1px solid var(--rule);height:52px}
  .field-label{display:block;font-size:12px;font-weight:300;color:var(--muted)}
  .field-value{display:block;font-size:17px;font-weight:300;margin-top:6px}
  .dots{letter-spacing:9px;font-size:16px;margin-top:4px}
  .chevron{position:absolute;right:4px;top:26px}
  .gender{position:absolute;left:32px;top:282px;width:341px}
  .segments{display:flex;margin-top:8px}
  .segment{flex:1;height:36px;display:flex;align-items:center;justify-content:center;font-size:17px;font-weight:300}
  .segment.is-active{background:var(--brand)}
  .signup-button{position:absolute;left:0;top:648px;width:100%;height:52px;background:var(--button);display:flex;align-items:center;justify-content:center;font-size:14px;font-weight:500;letter-spacing:.5px}
  .signup-button svg{position:absolute;right:22px;top:19px}
</style>
</head>
<body>
  <main class="screen">
    <div class="status-bar">
      <svg width="14" height="12" viewBox="0 0 14 12"><path d="M0 1h14L7 11z" fill="#fff"/></svg>
      <svg width="12" height="12" viewBox="0 0 12 12"><path d="M12 0v12H0z" fill="#fff"/></svg>
      <svg width="7" height="12" viewBox="0 0 7 12"><rect x="0" y="1" width="7" height="11" fill="#fff"/><rect x="2" y="0" width="3" height="1" fill="#fff"/></svg>
      <span class="time">12:30</span>
    </div>
    <header class="app-bar">
      <svg class="back" width="20" height="18" viewBox="0 0 20 18"><path d="M19 9H2M9 2L2 9l7 7" stroke="#cfd0d3" stroke-width="1.6" fill="none"/></svg>
      <span class="brand-name">VeloMarn</span>
    </header>

    <h1 class="title">Sign up</h1>

    <div class="hero-photo" role="img" aria-label="Photo of riders on white sport motorcycles leaning into a race track corner"></div>

    <div class="field" style="top:148px">
      <span class="field-label">Email address</span>
      <span class="field-value">leoberg789@postfeld.net</span>
    </div>
    <div class="field" style="top:212px">
      <span class="field-label">User name</span>
      <span class="field-value">Leo Berg</span>
    </div>

    <div class="gender">
      <span class="field-label">Gender</span>
      <div class="segments">
        <span class="segment is-active">Male</span>
        <span class="segment">Female</span>
        <span class="segment">Diverse</span>
      </div>
    </div>

    <div class="field" style="top:352px">
      <span class="field-label">Year of birth</span>
      <span class="field-value">1996</span>
      <svg class="chevron" width="12" height="8" viewBox="0 0 12 8"><path d="M1 1l5 5 5-5" stroke="#fff" stroke-width="1.4" fill="none"/></svg>
    </div>
    <div class="field" style="top:420px">
      <span class="field-label">Password</span>
      <span class="field-value dots">••••••••••</span>
    </div>
    <div class="field" style="top:488px">
      <span class="field-label">Confirm password</span>
      <span class="field-value dots">••••••••••</span>
    </div>

    <a class="signup-button">SIGN UP
      <svg width="8" height="14" viewBox="0 0 8 14"><path d="M1 1l6 6-6 6" stroke="#fff" stroke-width="1.4" fill="none"/></svg>
    </a>
  </main>
</body>
</html>
```